Simple web design project

We need a four page web design for a premier domestic cleaning company. We would like to see designs which use white and blue (the blue in the logo - which is attatched). Please could the tab for the pages be horizontal and at the top of the page. Our company logo is attached and should be included on each page. Ideally, we would like the foundations of each page to be the same, with the word content differing as required (word content attatched). Additionally we have attached a flyer which has been distributed to advertise our company. Please could all web designs illustrate the same professional message this flyer does.

Target Market(s)

females with higher than average income, aged 30-50. Have families and work 9-5.

Industry/Entity Type

It Company

Requirements
Must have
• logo on each page. Foundations of each page the same. phone number and email on the bottom of each page.
Should not have
• please no pictures of females cleaning.

```html
<!DOCTYPE html>
<html lang="en">
<head>
<meta charset="utf-8">
<title>Brookmere Cleaners – Premier Domestic Cleaners</title>
<link rel="stylesheet" href="https://fonts.googleapis.com/css2?family=Questrial&family=Arimo:wght@400;700&display=swap">
<style>
  :root {
    --blue-deep: #005a85;
    --blue-main: #0a7bb8;
    --blue-bright: #00b3d6;
    --blue-night: #063f5e;
    --paper: #f3f3f1;
    --rule: #dcdcda;
    --ink: #3a3a3a;
    --white: #ffffff;
    --tick-top: #4f8fcf;
    --tick-bottom: #1c5a9a;
  }
  * { margin: 0; padding: 0; box-sizing: border-box; }
  html, body { width: 1200px; height: 1029px; overflow: hidden; }
  body {
    position: relative;
    background: var(--paper);
    font-family: "Questrial", sans-serif;
    color: var(--ink);
  }
  .topbar {
    position: absolute; left: 0; top: 0; width: 1200px; height: 26px;
    background: var(--blue-deep);
    font-family: "Arimo", sans-serif; font-size: 9px; color: #d7ecf6;
  }
  .topbar .utility { position: absolute; left: 210px; top: 8px; }
  .topbar .contact { position: absolute; right: 235px; top: 8px; }
  .topbar .sep { margin: 0 4px; }
  .header {
    position: absolute; left: 0; top: 26px; width: 1200px; height: 332px;
    background: linear-gradient(to bottom, var(--blue-bright) 0%, #0896c8 18%, var(--blue-main) 40%, var(--blue-main) 100%);
    border-bottom: 2px solid #c8e6f2;
  }
  .header-fade {
    position: absolute; left: 0; top: 360px; width: 1200px; height: 40px;
    background: linear-gradient(to bottom, #c9c9c7, var(--paper));
  }
  .brand { position: absolute; left: 206px; top: 44px; color: var(--white); }
  .brand .name { font-size: 25px; letter-spacing: 0.2px; }
  .brand .tagline { font-size: 11px; margin-top: 8px; margin-left: 40px; }
  .main-nav {
    position: absolute; left: 573px; top: 62px; display: flex;
    font-family: "Arimo", sans-serif; font-weight: 700; font-size: 11.5px; color: var(--white);
  }
  .main-nav a {
    display: block; width: 104px; height: 34px; padding: 11px 0 0 11px;
    border-left: 1px solid rgba(255,255,255,0.18); color: inherit; text-decoration: none;
  }
  .hero {
    position: absolute; left: 205px; top: 135px; width: 791px; height: 321px;
    background: #dcdcdc; border: 1px solid #c4c4c4; padding: 7px;
    box-shadow: 0 14px 14px -10px rgba(0,0,0,0.25);
  }
  .hero-backdrop {
    width: 100%; height: 100%;
    background: linear-gradient(160deg, #9fcdee 0%, #bfe1f6 40%, #d9effb 100%);
  }
  .hero-photo {
    position: absolute; left: 374px; top: 34px; width: 384px; height: 245px;
    background: var(--white); padding: 8px;
    box-shadow: 0 4px 8px rgba(0,0,0,0.18);
  }
  .hero-photo div {
    width: 100%; height: 100%;
    background: linear-gradient(135deg, #eeeeee 0%, #d2d2d2 55%, #a9a9a9 100%);
  }
  .rule { position: absolute; left: 205px; width: 791px; height: 1px; background: var(--rule); }
  .intro { position: absolute; left: 210px; top: 524px; width: 780px; font-size: 15.5px; line-height: 19px; }
  .intro p + p { margin-top: 20px; }
  .why-title { position: absolute; left: 214px; top: 658px; font-family: "Arimo", sans-serif; font-weight: 700; font-size: 14.5px; color: #333; }
  .benefits { position: absolute; list-style: none; font-size: 15.5px; }
  .benefits li { height: 30.5px; display: flex; align-items: center; }
  .tick {
    width: 21px; height: 21px; margin-right: 8px; border-radius: 3px;
    background: linear-gradient(to bottom, var(--tick-top), var(--tick-bottom));
    display: flex; align-items: center; justify-content: center;
  }
  .closing { position: absolute; left: 205px; top: 823px; font-size: 15.5px; }
  .footer-fade {
    position: absolute; left: 0; top: 852px; width: 1200px; height: 27px;
    background: linear-gradient(to bottom, var(--paper), #c9c9c7);
  }
  .footer {
    position: absolute; left: 0; top: 879px; width: 1200px; height: 64px;
    background: var(--blue-main);
    font-family: "Arimo", sans-serif; font-size: 10.5px; color: #e3f2f9;
  }
  .footer-nav { position: absolute; left: 207px; top: 27px; display: flex; gap: 14px; }
  .footer-nav a { color: inherit; text-decoration: none; }
  .copyright { position: absolute; right: 205px; top: 26px; }
  .copyright span { margin-left: 10px; }
  .base {
    position: absolute; left: 0; top: 943px; width: 1200px; height: 86px;
    background: linear-gradient(to right, var(--blue-night) 0%, #0a7aa2 35%, #1aa7c9 50%, #0a7aa2 65%, var(--blue-night) 100%);
  }
</style>
</head>
<body>
  <div class="topbar">
    <div class="utility">home<span class="sep">|</span>contact us</div>
    <div class="contact">075-000-321-88<span class="sep">|</span>hello@brookmerecleaners.co.uk</div>
  </div>

  <header class="header">
    <div class="brand">
      <div class="name">Brookmere Cleaners</div>
      <div class="tagline">Premier Domestic Cleaners</div>
    </div>
    <nav class="main-nav">
      <a href="#">HOME</a>
      <a href="#">SERVICES</a>
      <a href="#">PRICES</a>
      <a href="#">CONTACT US</a>
    </nav>
  </header>
  <div class="header-fade"></div>

  <section class="hero">
    <div class="hero-backdrop" role="img" aria-label="Blue sky with soft clouds and water droplets"></div>
    <div class="hero-photo">
      <div role="img" aria-label="Bright white modern living room with fireplace, plants and staircase"></div>
    </div>
  </section>

  <div class="rule" style="top:487px"></div>

  <section class="intro">
    <p>Welcome to our website, we are a premier domestic cleaning company based in Hollowford, Wiltshire.</p>
    <p>Our vision is to supply households with a quality, tailored cleaning service, freeing up individuals spare time and replacing the stereotypical unreliable, inconsistent cleaners.</p>
  </section>

  <div class="rule" style="top:631px"></div>

  <h2 class="why-title">Why us:</h2>
  <ul class="benefits" style="left:206px; top:682px;">
    <li><span class="tick"><svg width="12" height="12" viewBox="0 0 12 12"><path d="M2 6.5 L4.8 9.5 L10 2.5" fill="none" stroke="#fff" stroke-width="1.8"/></svg></span>No contracts</li>
    <li><span class="tick"><svg width="12" height="12" viewBox="0 0 12 12"><path d="M2 6.5 L4.8 9.5 L10 2.5" fill="none" stroke="#fff" stroke-width="1.8"/></svg></span>Insured</li>
    <li><span class="tick"><svg width="12" height="12" viewBox="0 0 12 12"><path d="M2 6.5 L4.8 9.5 L10 2.5" fill="none" stroke="#fff" stroke-width="1.8"/></svg></span>Free quotes</li>
  </ul>
  <ul class="benefits" style="left:570px; top:682px;">
    <li><span class="tick"><svg width="12" height="12" viewBox="0 0 12 12"><path d="M2 6.5 L4.8 9.5 L10 2.5" fill="none" stroke="#fff" stroke-width="1.8"/></svg></span>Personalised service</li>
    <li><span class="tick"><svg width="12" height="12" viewBox="0 0 12 12"><path d="M2 6.5 L4.8 9.5 L10 2.5" fill="none" stroke="#fff" stroke-width="1.8"/></svg></span>We supply all equipment at no extra cost</li>
    <li><span class="tick"><svg width="12" height="12" viewBox="0 0 12 12"><path d="M2 6.5 L4.8 9.5 L10 2.5" fill="none" stroke="#fff" stroke-width="1.8"/></svg></span>Hassel free service</li>
  </ul>

  <div class="rule" style="top:797px"></div>

  <p class="closing">Have a look through our website to see how we can help you.</p>

  <div class="footer-fade"></div>
  <footer class="footer">
    <nav class="footer-nav">
      <a href="#">Home</a>
      <a href="#">Services</a>
      <a href="#">Prices</a>
      <a href="#">Contuct us</a>
    </nav>
    <div class="copyright">All rights reserved<span>2012</span></div>
  </footer>
  <div class="base"></div>
</body>
</html>
```